HL - business card

Harbor Lane Brokers is an insurance brokerage firm, inovative, proactive, vigorous, which aims to become the leader of the insurance brokers in Anfrica. We should like to get some designs which should be avoided also in Gray / Metallic for the Administration and Orange / Blue for the Managers (ike in the picture sent). The Blue / Green logo is not the correct one, but the source of the file. Please adjust the color accordingly for the business cards. 1 / Orange / Blue 2 / Gray / Metallic We want something classic but which is transmitted strenght, inovation, modernity and most of all, rapidity. We want something start-up like, very punchy and catching eye remaining profesional at the same time. Name: Tobias Wendell Function: Managing Director Address: N ° 17/18 Rua Dovel - R / C 2B Direita - Bairro Sambelo - Luanda Tel: (+244) 947 385 610 Email: tobias.wendell@harbor-l.com Website: www.harbor-l. com We want classic in the front and creative, colorfull at the back. The cards will be printed in relief, with very high quality of paper.
Insurance Broker
Designer to choose colors to be used in the design.

```html
<!DOCTYPE html>
<html lang="en">
<head>
<meta charset="utf-8">
<title>Harbor Lane Brokers – Business Card</title>
<link href="https://fonts.googleapis.com/css2?family=Montserrat:wght@400;500;600;700&display=swap" rel="stylesheet">
<style>
  :root {
    --backdrop: #8d8d8d;
    --brand-blue: #1d8fd0;
    --brand-blue-light: #35a9e3;
    --brand-blue-deep: #1677b8;
    --brand-orange: #f37b1d;
    --ink: #5c5c5c;
    --paper: #ffffff;
    --emblem-tint-top: #e4f1fa;
    --emblem-tint-bottom: #fdf0e4;
  }
  * { margin: 0; padding: 0; box-sizing: border-box; }
  html, body { width: 1200px; height: 930px; overflow: hidden; }
  body {
    background: radial-gradient(ellipse at 40% 35%, #b3b3b3 0%, var(--backdrop) 75%);
    font-family: "Montserrat", sans-serif;
    position: relative;
  }
  .card {
    position: absolute;
    width: 620px;
    height: 354px;
    border-radius: 22px;
    box-shadow: 0 10px 24px rgba(0,0,0,0.28);
    overflow: hidden;
  }
  /* Front */
  .card-front {
    left: 90px; top: 70px;
    background: linear-gradient(160deg, var(--brand-blue-light) 0%, var(--brand-blue-deep) 100%);
    display: flex; align-items: center; justify-content: center; gap: 16px;
  }
  .card-front .brand-dot {
    width: 34px; height: 34px; border-radius: 50%;
    background: var(--brand-orange);
    flex: none;
  }
  .card-front .brand-name {
    color: var(--paper);
    font-weight: 700;
    font-size: 30px;
    letter-spacing: 0.5px;
    text-transform: uppercase;
    white-space: nowrap;
  }
  /* Back */
  .card-back {
    left: 490px; top: 506px;
    background: var(--paper);
  }
  .emblem-area {
    position: absolute;
    right: 60px; top: -10px;
    width: 210px; height: 330px;
    border-radius: 50% 50% 40% 40%;
    background: linear-gradient(180deg, var(--emblem-tint-top) 0%, var(--emblem-tint-bottom) 100%);
    opacity: 0.8;
  }
  .back-brand {
    position: absolute; left: 40px; top: 56px;
    display: flex; align-items: center; gap: 10px;
  }
  .back-brand .brand-dot {
    width: 22px; height: 22px; border-radius: 50%;
    background: var(--brand-blue);
    flex: none;
  }
  .back-brand .brand-name {
    color: var(--brand-orange);
    font-weight: 700; font-size: 19px;
    text-transform: uppercase; letter-spacing: 0.3px;
    white-space: nowrap;
  }
  .holder {
    position: absolute; right: 40px; top: 138px;
    text-align: right;
  }
  .holder-name {
    color: var(--brand-blue);
    font-weight: 600; font-size: 24px;
    white-space: nowrap;
  }
  .holder-role {
    color: var(--ink);
    font-size: 12px; margin-top: 2px;
  }
  .divider {
    position: absolute; left: 40px; right: 40px; top: 212px;
    height: 1.5px; background: var(--brand-orange);
  }
  .address {
    position: absolute; right: 40px; top: 226px;
    text-align: right; color: var(--ink);
    font-size: 13px; line-height: 1.55; font-style: normal;
  }
  .contacts {
    position: absolute; left: 40px; bottom: 30px;
    color: var(--ink); font-size: 14px; line-height: 1.7;
    list-style: none;
  }
  .contacts li { display: flex; align-items: center; gap: 10px; white-space: nowrap; }
  .contacts svg { width: 13px; height: 13px; flex: none; }
</style>
</head>
<body>

  <section class="card card-front" aria-label="Card front">
    <span class="brand-dot"></span>
    <span class="brand-name">Harbor Lane Brokers</span>
  </section>

  <section class="card card-back" aria-label="Card back">
    <div class="emblem-area" role="img" aria-label="Faint brand emblem decoration"></div>

    <div class="back-brand">
      <span class="brand-dot"></span>
      <span class="brand-name">Harbor Lane Brokers</span>
    </div>

    <div class="holder">
      <div class="holder-name">Tobias Wendell</div>
      <div class="holder-role">Managing Director</div>
    </div>

    <div class="divider"></div>

    <address class="address">
      N° 17/18 Rua Dovel<br>
      R / C 2B Direita<br>
      Bairro Sambelo - Luanda
    </address>

    <ul class="contacts">
      <li>
        <svg viewBox="0 0 24 24" aria-hidden="true"><path fill="#f37b1d" d="M6.6 10.8a15.1 15.1 0 0 0 6.6 6.6l2.2-2.2a1 1 0 0 1 1-.25 11.4 11.4 0 0 0 3.6.57 1 1 0 0 1 1 1V20a1 1 0 0 1-1 1A17 17 0 0 1 3 4a1 1 0 0 1 1-1h3.5a1 1 0 0 1 1 1c0 1.25.2 2.45.57 3.57a1 1 0 0 1-.25 1z"/></svg>
        +244 947 385 610
      </li>
      <li>
        <svg viewBox="0 0 24 24" aria-hidden="true"><rect x="2.5" y="5" width="19" height="14" rx="2" fill="none" stroke="#f37b1d" stroke-width="2"/><path d="M3 6l9 7 9-7" fill="none" stroke="#f37b1d" stroke-width="2"/></svg>
        tobias.wendell@harbor-l.com
      </li>
    </ul>
  </section>

</body>
</html>
```